Business cards — need something that creates “wow” factor

Need a sleek and clean looking business card. Something that is clear and consise. These business cards are for my painting business and hundreds will be placed in the Dallas area between all Halbrook Fennimore paint stored. These card really need to stick out! Open to any and all ideas...

Target Market(s)

Residential clientele

Industry/Entity Type

Painting

Contact Information for Business Card

Galvin Otterly
Owner

582.316.0478

Web: Brightoakfinishes.com (still under construction)
Brightoakfinishes@mailbay.com

Font styles to use
Sans Serif

Colors

Designer to choose colors to be used in the design.

Requirements
Must have
• My name, number, website, email, Facebook
• and “100% customer satisfaction guaranteed”
• Facebook.com/Brightoakfinishes/
Nice to have
• Listed services
• Interior/exterior painting
• Drywall repair/texture
• Fence staining/refinishing
• Concrete staining
• Epoxy flooring
• Pressure washing

```html
<!DOCTYPE html>
<html lang="en">
<head>
<meta charset="utf-8">
<title>Brightoak Finishes — Business Card</title>
<link rel="stylesheet" href="https://fonts.googleapis.com/css2?family=Raleway:wght@400;500;700&display=swap">
<style>
  :root {
    --backdrop: #e9e7e8;
    --card-black: #1c1c1c;
    --card-white: #ffffff;
    --ink: #111111;
    --accent-yellow: #f7c21c;
    --muted: #bdbdbd;
  }
  * { box-sizing: border-box; margin: 0; padding: 0; }
  html, body { width: 1200px; height: 994px; overflow: hidden; }
  body {
    background: var(--backdrop);
    font-family: "Raleway", sans-serif;
    color: var(--ink);
    position: relative;
  }
  .card {
    position: absolute;
    width: 580px;
    height: 332px;
    box-shadow: 0 8px 24px rgba(0,0,0,0.18);
    overflow: hidden;
  }

  /* Back side */
  .card-back {
    left: 570px;
    top: 110px;
    background: var(--card-black);
  }
  .brand {
    position: absolute;
    left: 250px;
    top: 92px;
    width: 290px;
    text-align: center;
    color: #ffffff;
  }
  .brand-name {
    display: flex;
    align-items: center;
    justify-content: center;
    gap: 12px;
    font-weight: 500;
    font-size: 34px;
    letter-spacing: 1px;
    line-height: 1.1;
  }
  .brand-dot {
    width: 16px;
    height: 16px;
    border-radius: 50%;
    background: var(--accent-yellow);
    flex: none;
  }
  .brand-tagline {
    margin-top: 10px;
    font-size: 10px;
    font-weight: 400;
    letter-spacing: 0.5px;
    color: var(--muted);
  }
  .guarantee-tab {
    position: absolute;
    left: 120px;
    bottom: 0;
    width: 320px;
    height: 74px;
    background: var(--accent-yellow);
    border-radius: 28px 28px 0 0;
    display: flex;
    align-items: center;
    justify-content: center;
    font-size: 15px;
    font-weight: 500;
    color: var(--ink);
  }

  /* Front side */
  .card-front {
    left: 60px;
    top: 520px;
    background: var(--card-white);
  }
  .contact {
    position: absolute;
    left: 40px;
    top: 40px;
  }
  .person-name {
    font-size: 30px;
    font-weight: 400;
    line-height: 1.1;
  }
  .person-name strong { font-weight: 700; }
  .person-title {
    font-size: 16px;
    font-weight: 400;
    color: #333;
    margin-top: 4px;
  }
  .phone {
    display: flex;
    align-items: center;
    gap: 12px;
    margin-top: 18px;
    font-size: 28px;
    font-weight: 400;
    letter-spacing: 1px;
  }
  .contact-line {
    display: flex;
    align-items: center;
    gap: 10px;
    margin-top: 14px;
    font-size: 14px;
  }
  .contact-line + .contact-line { margin-top: 8px; }
  .divider {
    position: absolute;
    left: 360px;
    top: 44px;
    bottom: 44px;
    width: 1.5px;
    background: var(--ink);
  }
  .services {
    position: absolute;
    left: 384px;
    top: 110px;
    list-style: none;
    font-size: 13.5px;
    line-height: 1.7;
  }
  .services li::before {
    content: "";
    display: inline-block;
    width: 5px;
    height: 5px;
    border-radius: 50%;
    background: var(--ink);
    margin-right: 10px;
    vertical-align: middle;
  }
</style>
</head>
<body>

  <section class="card card-back">
    <div class="brand">
      <div class="brand-name"><span class="brand-dot"></span>Brightoak Finishes</div>
      <div class="brand-tagline">Commercial | Residential | Interior | Exterior</div>
    </div>
    <div class="guarantee-tab">100% customer satisfaction guaranteed</div>
  </section>

  <section class="card card-front">
    <div class="contact">
      <h1 class="person-name"><strong>Galvin</strong> Otterly</h1>
      <p class="person-title">Owner</p>
      <p class="phone">
        <svg width="32" height="32" viewBox="0 0 32 32" aria-hidden="true">
          <circle cx="16" cy="16" r="14.5" fill="none" stroke="#111" stroke-width="2"/>
          <path d="M12 9 l3 0 l1 4 l-2 1.5 q1.5 3 4 4.5 l1.5 -2 l4 1 l0 3 q-1 1.5 -3 1.5 q-6 -1 -9.5 -9 q-0.5 -3 1 -4.5z" fill="#111"/>
        </svg>
        582.316.0478
      </p>
      <p class="contact-line">
        <svg width="20" height="14" viewBox="0 0 20 14" aria-hidden="true">
          <rect x="0" y="0" width="20" height="14" fill="#111"/>
          <path d="M0 0 L10 8 L20 0" fill="none" stroke="#fff" stroke-width="1.4"/>
        </svg>
        Brightoakfinishes@mailbay.com
      </p>
      <p class="contact-line">
        <svg width="20" height="20" viewBox="0 0 20 20" aria-hidden="true">
          <g fill="none" stroke="#111" stroke-width="1.4">
            <circle cx="10" cy="10" r="8.5"/>
            <ellipse cx="10" cy="10" rx="4" ry="8.5"/>
            <line x1="1.5" y1="10" x2="18.5" y2="10"/>
            <line x1="3" y1="5.5" x2="17" y2="5.5"/>
            <line x1="3" y1="14.5" x2="17" y2="14.5"/>
          </g>
        </svg>
        www.Brightoakfinishes.com
      </p>
    </div>

    <div class="divider"></div>

    <ul class="services">
      <li>Interior/exterior painting</li>
      <li>Drywall repair/texture</li>
      <li>Fence staining/refinishing</li>
      <li>Concrete staining</li>
      <li>Epoxy flooring</li>
      <li>Pressure washing</li>
    </ul>
  </section>

</body>
</html>
```